Etiketten für Honiggläser gesucht
sehr kreativer Entwurf, in dem alle umfangreichen Vorgaben berücksichtigt wurden. q4712 ist sehr service- und lösungsorientiert. Arbeitet sehr schnell und exzellent.
Zielgruppe
Wir sind eine junge Hobbyimkerei und produzieren unsere eigenen Honigsorten. Zielgruppe ist jeder, der Honig mag.
Aufgabenstellung
Das zu entwerfende Etiketten_Design soll grundsätzlich ein „absoluter Hingucker“ werden, einen hohen Wiedererkennungswert besitzen, edel erscheinen und die Hochwertigkeit des Produktes zum Ausdruck bringen.
Im engeren Sinn sollen zwei voneinander unabhängige Etikettenteile entworfen werden, die aber im Design eine Einheit bilden sollen:
Beim ersten Teil handelt es sich um den sogenannten Gewährverschluss; er verbindet den Deckel mit dem Glas und zerreißt beim ersten Öffnen des Deckels. Der Gewährverschluss soll etwa 2 cm breit und 8 cm lang sein, und unter anderem von unserem Firmenlogo (siehe Datei) geziert werden. Bei dem Logo darf die Grafik und der Hintergrund in der Farbe variieren, und der Schriftzug kann entfallen, andere Änderungen dürfen jedoch nicht vorgenommen werden. Das Logo kann bei Bedarf gerne in anderen Dateiformaten zur Verfügung gestellt werden.
Den zweiten Teil stellt das eigentliche Produktetikett dar. Für dieses gibt es keine Größen- und Formvorgaben, allerdings müssen folgende Inhalte Berücksichtigung finden: Die Daten des Imkers (bitte folgende Platzhalter verwenden „Firmenname“, „Vorname1 & Vorname2 Nachname“, „Straße + Hausnummer“, „PLZ + Ortsname“, „Internetseite“ und „Emailadresse“) sowie den Angaben „500g“, „Mindestens haltbar bis:“ (dahinter oder darunter bitte weißen Freiraum für den Stempelaufdruck des Datums lassen), „Trocken, dunkel und vor Wärme geschützt lagern!“, und – ganz wichtig – die „Honigsorte“ mit den vorangestellten Worten „feinster deutscher“ (, z.B. „feinster deutscher Rapshonig“).
Jede Honigsorte soll mit einer Farbe verknüpft werden, sodass der Kunde schnell erkennen kann um welche Honigsorte es sich im Glas handelt (beispielsweise gelb für Rapshonig, grün für Waldhonig, usw.). Dafür soll die jeweilige Honigsortenfarbe, in welcher Form auch immer, das Etikett oder einen bestimmten Bereich davon domini..

```html
<!DOCTYPE html>
<html lang="de">
<head>
<meta charset="utf-8">
<title>Honigetiketten – Imkerei Lindholt</title>
<link rel="stylesheet" href="https://fonts.googleapis.com/css2?family=Dancing+Script:wght@500&family=Kalam:wght@700&family=Marcellus&family=Open+Sans:wght@400&display=swap">
<style>
  :root {
    --paper: #ffffff;
    --ink: #1e1e1e;
    --ink-soft: #3a3a3a;
    --himbeer: #b8154a;
    --wald: #3a8c55;
    --seal: #141414;
  }
  html, body {
    margin: 0;
    width: 1200px;
    height: 848px;
    overflow: hidden;
    background: var(--paper);
  }
  .canvas {
    position: relative;
    width: 1200px;
    height: 848px;
  }
  .seal-strip {
    position: absolute;
    left: 280px;
    top: 150px;
    width: 66px;
    height: 420px;
  }
  .label {
    position: absolute;
    width: 372px;
    height: 246px;
  }
  .label--himbeer { left: 723px; top: 162px; --variety: var(--himbeer); }
  .label--wald    { left: 717px; top: 445px; --variety: var(--wald); }
  .label svg { width: 100%; height: 100%; display: block; overflow: visible; }
  .label__rim { fill: var(--paper); stroke: var(--variety); stroke-width: 8; }
  .label__inner { fill: none; stroke: var(--ink-soft); stroke-width: 1.2; }
  .label__claim { font-family: "Dancing Script", cursive; font-size: 44px; fill: var(--ink); }
  .label__small { font-family: "Open Sans", sans-serif; font-size: 10.5px; fill: var(--ink-soft); }
  .label__contact { font-family: "Open Sans", sans-serif; font-size: 13px; fill: var(--ink-soft); letter-spacing: 0.4px; }
  .label__weight { font-family: "Open Sans", sans-serif; font-size: 22px; fill: var(--ink); }
  .label__date-box { fill: var(--paper); stroke: var(--ink-soft); stroke-width: 1.2; }
  .label__mark { fill: none; stroke: var(--ink); stroke-width: 5; }
  .label__brand { font-family: "Marcellus", serif; font-size: 30px; fill: var(--ink); letter-spacing: 3px; }
  .label__variety { font-family: "Kalam", cursive; font-weight: 700; font-size: 52px; fill: var(--variety); letter-spacing: 2px; }
</style>
</head>
<body>
<main class="canvas">

  <svg class="seal-strip" viewBox="0 0 66 420" aria-label="Gewährverschluss">
    <polygon points="0,0 66,0 66,420 33,380 0,420" fill="var(--seal)"/>
  </svg>

  <section class="label label--himbeer">
    <svg viewBox="0 0 620 410">
      <defs>
        <path id="claim-arc-h" d="M78,150 Q310,-20 545,150"/>
        <path id="variety-arc-h" d="M150,320 Q315,395 480,310"/>
      </defs>
      <ellipse class="label__rim" cx="310" cy="205" rx="302" ry="197"/>
      <ellipse class="label__inner" cx="310" cy="205" rx="290" ry="184"/>
      <text class="label__claim"><textPath href="#claim-arc-h" startOffset="50%" text-anchor="middle">feinster deutscher Rapshonig</textPath></text>
      <text class="label__small" x="37" y="184">Trocken, dunkel und vor</text>
      <text class="label__small" x="37" y="199">Wärme geschützt lagern</text>
      <text class="label__small" x="37" y="218">Mindestens haltbar bis:</text>
      <rect class="label__date-box" x="37" y="225" width="118" height="25" rx="2"/>
      <text class="label__weight" x="60" y="280">500G.</text>
      <text class="label__contact" x="572" y="168" text-anchor="end">Birkenweg 14</text>
      <text class="label__contact" x="572" y="187" text-anchor="end">3012 Bern</text>
      <text class="label__contact" x="572" y="206" text-anchor="end">www.imkereilindholt.de</text>
      <text class="label__contact" x="572" y="225" text-anchor="end">@imkereilindholt.de</text>
      <circle class="label__mark" cx="305" cy="160" r="58"/>
      <text class="label__brand" x="305" y="258" text-anchor="middle">IMKEREI</text>
      <text class="label__brand" x="305" y="292" text-anchor="middle">LINDHOLT</text>
      <text class="label__variety"><textPath href="#variety-arc-h" startOffset="50%" text-anchor="middle">Himbeerhonig</textPath></text>
    </svg>
  </section>

  <section class="label label--wald">
    <svg viewBox="0 0 620 410">
      <defs>
        <path id="claim-arc-w" d="M78,150 Q310,-20 545,150"/>
        <path id="variety-arc-w" d="M185,320 Q315,390 445,312"/>
      </defs>
      <ellipse class="label__rim" cx="310" cy="205" rx="302" ry="197"/>
      <ellipse class="label__inner" cx="310" cy="205" rx="290" ry="184"/>
      <text class="label__claim"><textPath href="#claim-arc-w" startOffset="50%" text-anchor="middle">feinster deutscher Rapshonig</textPath></text>
      <text class="label__small" x="37" y="184">Trocken, dunkel und vor</text>
      <text class="label__small" x="37" y="199">Wärme geschützt lagern</text>
      <text class="label__small" x="37" y="218">Mindestens haltbar bis:</text>
      <rect class="label__date-box" x="37" y="225" width="118" height="25" rx="2"/>
      <text class="label__weight" x="60" y="280">500G.</text>
      <text class="label__contact" x="572" y="168" text-anchor="end">Birkenweg 14</text>
      <text class="label__contact" x="572" y="187" text-anchor="end">3012 Bern</text>
      <text class="label__contact" x="572" y="206" text-anchor="end">www.imkereilindholt.de</text>
      <text class="label__contact" x="572" y="225" text-anchor="end">@imkereilindholt.de</text>
      <circle class="label__mark" cx="305" cy="160" r="58"/>
      <text class="label__brand" x="305" y="258" text-anchor="middle">IMKEREI</text>
      <text class="label__brand" x="305" y="292" text-anchor="middle">LINDHOLT</text>
      <text class="label__variety"><textPath href="#variety-arc-w" startOffset="50%" text-anchor="middle">Waldhonig</textPath></text>
    </svg>
  </section>

</main>
</body>
</html>
```